kf novum
My service company has specialists in Sales, Marketing and Change Management. Our target group is the 1st and 2nd management level of enterprises, who want to align their strategy at new market situations or to change their distribution, communication or product concept.
We help our clients in defined time frames or projects not only in defining new strategies and concepts but also in implementation and measurements of the results.
I'm looking for a design of business cards and A4 letter paper. The company name is "kf novum"; my name ist Konrad Fels...
So the name of my company stands for Management on time (kf novum) and kf stands for my name (initials)
Logo see enclosed.

```html
<!DOCTYPE html>
<html lang="de">
<head>
<meta charset="utf-8">
<title>kf novum – Briefbogen</title>
<link href="https://fonts.googleapis.com/css2?family=Michroma&display=swap" rel="stylesheet">
<style>
  :root {
    --backdrop: #75777a;
    --paper: #ffffff;
    --ink: #1f2530;
    --ink-soft: #4a4e55;
    --mark: #1f2530;
  }
  html, body {
    margin: 0;
    padding: 0;
    width: 900px;
    height: 1200px;
    overflow: hidden;
    background: var(--backdrop);
  }
  .sheet {
    position: absolute;
    left: 56px;
    top: 43px;
    width: 787px;
    height: 1114px;
    background: var(--paper);
    font-family: "Michroma", sans-serif;
    color: var(--ink-soft);
  }
  .brand-name {
    position: absolute;
    right: 40px;
    top: 122px;
    margin: 0;
    font-size: 25px;
    font-weight: 400;
    letter-spacing: 0.5px;
    color: var(--ink);
    line-height: 1;
  }
  .sender-line {
    position: absolute;
    left: 93px;
    top: 186px;
    font-size: 6.5px;
    color: var(--ink-soft);
    letter-spacing: 0.1px;
  }
  .fold-mark {
    position: absolute;
    left: 8px;
    width: 12px;
    height: 0;
    border-top: 0.8px solid var(--mark);
  }
  .fold-mark.upper { top: 393px; }
  .fold-mark.punch { top: 556px; }
  .fold-mark.lower { top: 787px; }
  .contact {
    position: absolute;
    left: 587px;
    top: 950px;
    font-size: 8.4px;
    line-height: 16px;
    letter-spacing: 0.9px;
    color: var(--ink-soft);
    font-style: normal;
  }
  .contact-group {
    position: relative;
    padding-left: 25px;
  }
  .contact-group + .contact-group { margin-top: 5px; }
  .contact-row { position: relative; white-space: nowrap; }
  .contact-row svg {
    position: absolute;
    left: -25px;
    top: 3px;
    width: 10px;
    height: 10px;
    fill: var(--ink);
  }
  .contact-name {
    color: var(--ink);
    -webkit-text-stroke: 0.35px var(--ink);
  }
</style>
</head>
<body>
<main class="sheet">
  <h1 class="brand-name">kf novum</h1>

  <div class="sender-line">kf novum · Musterstraße 12 · 12345 Musterstadt</div>

  <span class="fold-mark upper"></span>
  <span class="fold-mark punch"></span>
  <span class="fold-mark lower"></span>

  <address class="contact">
    <div class="contact-group">
      <div class="contact-row contact-name">
        <svg viewBox="0 0 10 10" aria-hidden="true"><path d="M5 0.3a3.3 3.3 0 0 0-3.3 3.3C1.7 6 5 9.7 5 9.7S8.3 6 8.3 3.6A3.3 3.3 0 0 0 5 0.3zm0 4.6a1.3 1.3 0 1 1 0-2.6 1.3 1.3 0 0 1 0 2.6z"/></svg>
        kf novum
      </div>
      <div class="contact-row">Konrad Fels</div>
      <div class="contact-row">Musterstrasse 12</div>
      <div class="contact-row">12345 Musterstadt</div>
    </div>
    <div class="contact-group">
      <div class="contact-row">
        <svg viewBox="0 0 10 10" aria-hidden="true"><path d="M2.2 0.6l1.6 2.1-1 1.1c.6 1.3 1.7 2.4 3 3l1.1-1 2.1 1.6-.9 1.9C4.4 9 1 5.6.4 1.5z"/></svg>
        +49 3041 7720568
      </div>
      <div class="contact-row">
        <svg viewBox="0 0 10 10" aria-hidden="true"><path d="M2.6 0h4.8c.5 0 .8.3.8.8v8.4c0 .5-.3.8-.8.8H2.6c-.5 0-.8-.3-.8-.8V.8c0-.5.3-.8.8-.8zm.4 1.2v6.6h4V1.2zm2 7.2a.5.5 0 1 0 0 1 .5.5 0 0 0 0-1z"/></svg>
        +49 160 9382714
      </div>
    </div>
    <div class="contact-group">
      <div class="contact-row">
        <svg viewBox="0 0 10 10" aria-hidden="true"><path d="M5 .5a4.5 4.5 0 1 0 0 9 4.5 4.5 0 0 0 0-9zm3.4 4H6.9a7 7 0 0 0-.6-2.8A3.5 3.5 0 0 1 8.4 4.5zM5 1.6c.5.6.9 1.7.9 2.9H4.1c0-1.2.4-2.3.9-2.9zM3.7 1.7a7 7 0 0 0-.6 2.8H1.6a3.5 3.5 0 0 1 2.1-2.8zM1.6 5.5h1.5c0 1 .2 2 .6 2.8a3.5 3.5 0 0 1-2.1-2.8zM5 8.4c-.5-.6-.9-1.7-.9-2.9h1.8c0 1.2-.4 2.3-.9 2.9zm1.3-.1a7 7 0 0 0 .6-2.8h1.5a3.5 3.5 0 0 1-2.1 2.8z"/></svg>
        www.kfnovum.com
      </div>
      <div class="contact-row">
        <svg viewBox="0 0 10 10" aria-hidden="true"><path d="M.5 2h9v.6L5 5.6.5 2.6zm0 1.8L5 6.8l4.5-3V8H.5z"/></svg>
        info@kfnovum.com
      </div>
    </div>
  </address>
</main>
</body>
</html>
```